Online campaigning platform needs web design

We need designs for our start a survey page and company overview page (undesigned elements attached). Our platform allows people to crowd-source better workplace policies and push them to become a reality.
The company name is Tallyhive Platform and the primary colour is teal, with secondary colours of white, dark grey and green. The company logo is attached.
Website needs to be modern, clean and simple. As part of the design I would like to see iconography representing concepts like: secure, safety in numbers, teamwork, registration, insights (or results) and email.
We will provide feedback regardless of the quality of the design to ensure a better outcome for all parties.
Please feel free to contact us if you have any questions.
# The designer can use placeholder images or feel free to use any/all or none of the attached images
# The designer can use sample filler text
Under 40s
It Company
2 page

```html
<!DOCTYPE html>
<html lang="en">
<head>
<meta charset="utf-8">
<title>Tallyhive Platform – Overview</title>
<link rel="stylesheet" href="https://fonts.googleapis.com/css2?family=Comfortaa:wght@300;400&display=swap">
<style>
  :root {
    --teal: #14a89c;
    --sky: #03a7c5;
    --white: #ffffff;
    --ink: #58595b;
    --nav-ink: #4d4d4f;
    --photo-light: #c9d3dd;
    --photo-dark: #2f3e5e;
  }
  * { box-sizing: border-box; margin: 0; padding: 0; }
  html, body {
    width: 1163px;
    height: 1200px;
    overflow: hidden;
    background: var(--white);
    font-family: "Comfortaa", sans-serif;
    font-weight: 300;
  }
  .page { position: relative; width: 1163px; height: 1200px; }

  .site-header {
    position: absolute; left: 0; top: 0; width: 100%; height: 90px;
    background: var(--white);
  }
  .brand {
    position: absolute; left: 24px; top: 24px;
    display: flex; align-items: center; gap: 10px;
    color: var(--sky); font-weight: 400; font-size: 21px; line-height: 1.05;
    letter-spacing: -0.5px; text-decoration: none;
  }
  .brand-dot { width: 14px; height: 14px; border-radius: 50%; background: var(--sky); }
  .main-nav {
    position: absolute; top: 46px; right: 43px;
    display: flex; gap: 16px;
  }
  .main-nav a {
    color: var(--nav-ink); text-decoration: none;
    font-size: 15px; font-weight: 400; letter-spacing: -0.3px;
  }

  .hero {
    position: absolute; left: 0; top: 90px; width: 100%; height: 243px;
    background: var(--teal); color: var(--white);
  }
  .welcome {
    position: absolute; right: 46px; top: 11px;
    font-size: 17px; letter-spacing: 0.3px;
  }
  .hero-title {
    position: absolute; left: 0; right: 0; top: 100px;
    text-align: center; font-size: 44px; font-weight: 300;
  }

  .overview {
    position: absolute; left: 0; top: 333px; width: 100%; height: 409px;
    background: var(--white);
  }
  .overview-copy {
    position: absolute; left: 247px; top: 34px; width: 710px;
    color: var(--ink); font-size: 13px; line-height: 16.8px; text-align: justify;
  }
  .overview-copy p + p { margin-top: 17px; }
  .action {
    position: absolute; top: 300px; width: 192px; height: 47px;
    background: var(--teal); color: var(--white);
    display: flex; align-items: center; justify-content: center;
    font-size: 27px; text-decoration: none;
  }
  .action-campaigns { left: 312px; }
  .action-surveys { left: 667px; }

  .history {
    position: absolute; left: 0; top: 742px; width: 100%; height: 458px;
    background: var(--sky); color: var(--white);
  }
  .history-title {
    position: absolute; left: 0; width: 1117px; top: 25px;
    text-align: center; font-size: 34px; font-weight: 300;
  }
  .history-photo {
    position: absolute; left: 126px; top: 84px; width: 241px; height: 220px;
    background: linear-gradient(135deg, var(--photo-light) 0%, #8796ad 45%, var(--photo-dark) 100%);
  }
  .history-copy {
    position: absolute; left: 397px; top: 86px; width: 720px;
    font-size: 13px; line-height: 16.8px; text-align: justify;
  }
  .history-copy p + p { margin-top: 17px; }
</style>
</head>
<body>
<div class="page">
  <header class="site-header">
    <a class="brand" href="#"><span class="brand-dot"></span><span>TALLYHIVE<br>PLATFORM</span></a>
    <nav class="main-nav">
      <a href="#">HOME</a>
      <a href="#">OVERVIEW</a>
      <a href="#">HISTORY</a>
      <a href="#">JOIN US</a>
      <a href="#">OUR REACH</a>
    </nav>
  </header>

  <section class="hero">
    <p class="welcome">Welcome Daniel Marsh</p>
    <h1 class="hero-title">Overview</h1>
  </section>

  <section class="overview">
    <div class="overview-copy">
      <p>It is a long established fact that a reader will be distracted by the readable content of a page when looking at its layout. The point of using Lorem Ipsum is that it has a more-or-less normal distribution of letters, as opposed to using 'Content here, content here', making it look like readable English. Many desktop publishing packages and web page editors now use Lorem Ipsum as their default model text, and a search for 'lorem ipsum' will uncover many web sites still in their infancy. Various versions have evolved over the years, sometimes by accident, sometimes on purpose (injected humour and the like)</p>
      <p>It is a long established fact that a reader will be distracted by the readable content of a page when looking at its layout. The point of using Lorem Ipsum is that it has a more-or-less normal distribution of letters, as opposed to using 'Content here, content here', making it look like readable English. Many desktop publishing packages and web page editors now use Lorem Ipsum as their default model text, and a search for 'lorem ipsum' will uncover many web sites still in their infancy. Various versions have evolved over the years, sometimes by accident, sometimes on purpose (injected humour and the like)</p>
    </div>
    <a class="action action-campaigns" href="#">Campaigns</a>
    <a class="action action-surveys" href="#">Surveys</a>
  </section>

  <section class="history">
    <h2 class="history-title">Our History</h2>
    <div class="history-photo" role="img" aria-label="Photo of a businessman in a suit working at a desk with papers and a glass of water"></div>
    <div class="history-copy">
      <p>It is a long established fact that a reader will be distracted by the readable content of a page when looking at its layout. The point of using Lorem Ipsum is that it has a more-or-less normal distribution of letters, as opposed to using 'Content here, content here', making it look like readable English. Many desktop publishing packages and web page editors now use Lorem Ipsum as their default model text, and a search for 'lorem ipsum' will uncover many web sites still in their infancy. Various versions have evolved over the years, sometimes by accident, sometimes on purpose (injected humour and the like)</p>
      <p>It is a long established fact that a reader will be distracted by the readable content of a page when looking at its layout. The point of using Lorem Ipsum is that it has a more-or-less normal distribution of letters, as opposed to using 'Content here, content here', making it look like readable English. Many desktop publishing packages and web page editors now use Lorem Ipsum as their default model text, and a search for 'lorem ipsum' will uncover many web sites still in their infancy. Various versions have evolved over the years, sometimes by accident, sometimes on purpose (injected humour and the like)</p>
    </div>
  </section>
</div>
</body>
</html>
```